I need a business card design for a new company that will be doing consulting work around issues of cultural competency, and diversity and inclusion. I would like the design to be crisp and clear with bold but conservative colors and incorporate shades of blue

Target Market(s)

Small businesses, schools, non-profits

Industry/Entity Type

Consulting

Font styles to use
Serif
Sans Serif

Colors
0c5ba6
6b449b
3276b5
0292cd

Requirements
Must have
• A Morrow Venture (name of company)
• Lemlem Tavish
• CEO
• lemlem@amorrowventure.com
• (215)483-2756

```html
<!DOCTYPE html>
<html lang="en">
<head>
<meta charset="utf-8">
<title>A Morrow Venture — Business Card</title>
<link rel="stylesheet" href="https://fonts.googleapis.com/css2?family=Fira+Sans+Condensed:wght@300;600;700&family=Open+Sans:wght@400&display=swap">
<style>
  :root {
    --paper: #ffffff;
    --brand-violet: #4b2cf5;
    --panel-blue: #1b55f3;
    --tab-sky: #38b2f7;
    --tab-edge: #2a9ee6;
    --ink-light: #ffffff;
  }
  * { margin: 0; padding: 0; box-sizing: border-box; }
  html, body { width: 1200px; height: 720px; overflow: hidden; background: var(--paper); }
  .card {
    position: relative;
    width: 1200px;
    height: 720px;
    background: var(--paper);
    overflow: hidden;
  }
  .brand-side {
    position: absolute;
    left: 0; top: 0;
    width: 600px; height: 720px;
    display: flex;
    align-items: center;
    justify-content: center;
  }
  .company-name {
    font-family: "Fira Sans Condensed", sans-serif;
    font-weight: 700;
    font-size: 62px;
    color: var(--brand-violet);
    letter-spacing: 0.5px;
    margin-top: -20px;
  }
  .contact-side {
    position: absolute;
    left: 600px; top: 0;
    width: 600px; height: 720px;
    background: var(--panel-blue);
  }
  .identity {
    position: absolute;
    left: 600px; top: 150px;
    width: 560px;
    text-align: center;
    color: var(--ink-light);
    font-family: "Fira Sans Condensed", sans-serif;
  }
  .person-name { font-weight: 600; font-size: 45px; line-height: 1.1; }
  .person-role { font-weight: 300; font-size: 40px; line-height: 1.1; }
  .tab {
    position: absolute;
    left: 584px; top: 368px;
    width: 70px; height: 272px;
  }
  .contact-list {
    position: absolute;
    left: 600px; top: 458px;
    list-style: none;
    font-family: "Open Sans", sans-serif;
    font-size: 35px;
    color: var(--ink-light);
  }
  .contact-item {
    display: flex;
    align-items: center;
    height: 58px;
  }
  .contact-icon {
    width: 44px;
    display: flex;
    justify-content: center;
    margin-left: 0;
    margin-right: 15px;
    font-family: "Fira Sans Condensed", sans-serif;
    font-weight: 700;
    font-size: 36px;
  }
</style>
</head>
<body>
  <main class="card">
    <section class="brand-side">
      <h1 class="company-name">A Morrow Venture</h1>
    </section>

    <section class="contact-side"></section>

    <svg class="tab" viewBox="0 0 70 272" aria-hidden="true">
      <polygon points="0,2 14,12 14,260 0,270" fill="var(--tab-edge)"/>
      <polygon points="14,12 67,30 67,244 14,260" fill="var(--tab-sky)"/>
    </svg>

    <header class="identity">
      <p class="person-name">Lemlem Tavish</p>
      <p class="person-role">CEO</p>
    </header>

    <ul class="contact-list">
      <li class="contact-item">
        <span class="contact-icon">
          <svg width="34" height="34" viewBox="0 0 34 34" aria-hidden="true">
            <path d="M9 4 h6 l1 8 -4 2 c1 3 1 6 0 8 l4 2 -1 8 h-6 c-5-6-5-22 0-28z" fill="var(--ink-light)"/>
            <path d="M21 12 q3 5 0 10" stroke="var(--ink-light)" stroke-width="2.6" fill="none" stroke-linecap="round"/>
            <path d="M26 8 q5 9 0 18" stroke="var(--ink-light)" stroke-width="2.6" fill="none" stroke-linecap="round"/>
          </svg>
        </span>
        <span class="contact-text">(215)483-2756</span>
      </li>
      <li class="contact-item">
        <span class="contact-icon">@</span>
        <span class="contact-text">lemlem@amorrowventure.com</span>
      </li>
    </ul>
  </main>
</body>
</html>
```